Harbor LunaVital & Equipments

I need to create full stationery design for the company; Business Card, Envelop, Letterheads, Calendar and email template.

Our company is specialized in the import and export of nutritional, pharmaceutical and cosmetics in addition to medical equipments.

These is no limitation on how to use colors within the design.

Target Market(s)

Global

Industry/Entity Type

Healthcare

Other font styles liked:
• a font close to logo. Letterhead body text to be different than the address text

Requirements
Nice to have
• We will have multiple locations so it is good to keep space for future addresses.
• Stationary requirements:
• Letterhead: A4
• Envelopes: 3 regular sizes : large, medium and small (i do not know the sizes)
• Colors: extracted from the logo

```html
<!DOCTYPE html>
<html lang="en">
<head>
<meta charset="utf-8">
<title>Harbor LunaVital &amp; Equipments – Letterhead</title>
<link rel="stylesheet" href="https://fonts.googleapis.com/css2?family=Nunito:wght@800&family=Open+Sans:wght@400;600&family=Tinos:ital@0;1&display=swap">
<style>
  :root {
    --backdrop: #ececec;
    --paper: #ffffff;
    --brand-blue: #229bd2;
    --brand-navy: #14145a;
    --ink: #1d1d1d;
    --ink-soft: #333;
    --signature-tone: #c9c9c9;
  }
  * { margin: 0; padding: 0; box-sizing: border-box; }
  html, body { width: 1200px; height: 795px; overflow: hidden; background: var(--backdrop); }
  .letterhead {
    position: absolute; left: 338px; top: 28px;
    width: 523px; height: 740px;
    background: var(--paper);
    box-shadow: 0 2px 10px rgba(0,0,0,.12);
    overflow: hidden;
  }
  .brand {
    position: absolute; left: 40px; top: 46px;
    display: flex; align-items: center; gap: 8px;
  }
  .brand-square { width: 16px; height: 16px; background: var(--brand-blue); }
  .brand-name {
    font-family: "Nunito", sans-serif; font-weight: 800;
    font-size: 15px; color: var(--brand-blue); letter-spacing: .2px;
  }
  .letter {
    position: absolute; left: 40px; top: 160px; width: 385px;
    font-family: "Tinos", serif; font-size: 9.6px; line-height: 1.42;
    color: var(--ink);
  }
  .letter .greeting { margin-bottom: 8px; }
  .letter p { text-align: justify; text-indent: 10px; margin-bottom: 12px; }
  .signoff {
    position: absolute; left: 232px; top: 420px;
    font-family: "Tinos", serif; font-size: 9.6px; line-height: 1.45; color: var(--ink);
  }
  .signature {
    width: 90px; height: 30px; margin: 4px 0 4px;
    background: linear-gradient(90deg, transparent, var(--signature-tone) 30%, var(--signature-tone) 70%, transparent);
    opacity: .5; border-radius: 12px;
  }
  .contact {
    position: absolute; left: 40px; top: 600px;
    font-family: "Open Sans", sans-serif; font-size: 9.6px; line-height: 1.5; color: var(--ink-soft);
  }
  .contact-row { display: flex; align-items: center; gap: 6px; margin-top: 3px; }
  .contact-row svg { width: 10px; height: 10px; flex: none; }
  .footer-wave { position: absolute; left: 0; bottom: 0; width: 523px; height: 120px; }
  .website {
    position: absolute; right: 26px; bottom: 28px;
    font-family: "Open Sans", sans-serif; font-size: 11px; color: #fff; letter-spacing: .3px;
  }
</style>
</head>
<body>
<main class="letterhead">
  <header class="brand">
    <span class="brand-square"></span>
    <span class="brand-name">Harbor LunaVital &amp; Equipments</span>
  </header>

  <section class="letter">
    <div class="greeting">Gentlemen,</div>
    <p>Enclosed please find the product catalogue we promised during our meeting last month. We would be pleased if you could review the listed nutritional and cosmetic lines and let us know which items suit your clinics. Our team can prepare samples within two weeks of your reply, and shipping terms remain as agreed. Should you need further details on pricing or certification, we will gladly send them, leaving all final choices to your own judgement.</p>
    <p>Would you also be kind enough to confirm the delivery address for the medical equipment order? Our records show two possible sites, and we wish to avoid any delay at customs. The diagnostic units were tested last week and passed every inspection, so they are ready to leave our warehouse. We have included the full technical sheets and the warranty terms with this letter. If any point is unclear, our export desk will answer promptly. We look forward to many years of good work together and hope to visit you soon.</p>
  </section>

  <section class="signoff">
    <div>In the meantime I remain</div>
    <div>Yours very truly,</div>
    <div class="signature" role="img" aria-label="Handwritten signature"></div>
    <div>Julian Marsh Corwin</div>
  </section>

  <address class="contact" style="font-style:normal">
    <div>1780 Meridian Avenue, Port Alder,</div>
    <div>Westhaven 40217</div>
    <div class="contact-row">
      <svg viewBox="0 0 10 10" aria-hidden="true"><path d="M2 1h2l1 2-1.2 1a5 5 0 0 0 2.2 2.2L7 5l2 1v2c0 .6-.4 1-1 1A8 8 0 0 1 1 2c0-.6.4-1 1-1z" fill="var(--brand-navy)"/></svg>
      <span>07800314729</span>
    </div>
    <div class="contact-row">
      <svg viewBox="0 0 10 10" aria-hidden="true"><rect x=".5" y="2" width="9" height="6.5" fill="none" stroke="var(--brand-navy)" stroke-width="1.2"/><path d="M.8 2.3 5 5.8l4.2-3.5" fill="none" stroke="var(--brand-navy)" stroke-width="1.2"/></svg>
      <span>info@harborlunavital.com</span>
    </div>
  </address>

  <svg class="footer-wave" viewBox="0 0 523 120" preserveAspectRatio="none" aria-hidden="true">
    <path d="M0 120 L0 112 C180 104 360 78 523 22 L523 120 Z" fill="var(--brand-blue)"/>
    <path d="M0 107 C180 99 355 70 523 10" fill="none" stroke="var(--brand-navy)" stroke-width="3.5"/>
  </svg>
  <div class="website">www.harborlunavital.com</div>
</main>
</body>
</html>
```